Lorvena Aesthetic Doctor

I require an elegant, luxurious looking business card for my aesthetic business. I am a doctor and that will set me aside from competitors. I am planning to provide home and spa based treatments to clients with high expectations. I have attached my logo.

```html
<!DOCTYPE html>
<html lang="en">
<head>
<meta charset="utf-8">
<title>Lorvena Aesthetic Doctor – Business Card</title>
<link href="https://fonts.googleapis.com/css2?family=Roboto:wght@400;500&display=swap" rel="stylesheet">
<style>
  :root {
    --backdrop: #3c3f42;
    --card-blue: #0f7dcb;
    --sky: #53b8e8;
    --pale-sky: #a8dcf2;
    --mist-grey: #a6a8ab;
    --logo-grey: #9c9ea1;
    --white: #ffffff;
  }
  * { margin: 0; padding: 0; box-sizing: border-box; }
  html, body { width: 1200px; height: 801px; overflow: hidden; }
  body {
    background: var(--backdrop);
    font-family: "Roboto", Arial, sans-serif;
    position: relative;
  }
  .card {
    position: absolute;
    top: 274px;
    width: 443px;
    height: 263px;
    overflow: hidden;
  }
  .card-front { left: 153px; background: var(--card-blue); color: var(--white); }
  .card-back { left: 625px; background: var(--white); }

  .portrait-art {
    position: absolute;
    left: 0; top: 0;
    width: 204px; height: 263px;
    background: linear-gradient(160deg, var(--pale-sky) 0%, var(--sky) 45%, #2a9ad9 70%, var(--pale-sky) 100%);
    border-top-right-radius: 120px 150px;
    border-bottom-right-radius: 70px 100px;
  }

  .details {
    position: absolute;
    right: 29px;
    top: 42px;
    text-align: right;
  }
  .doctor-name { font-size: 19px; font-weight: 500; line-height: 1; white-space: nowrap; }
  .doctor-name .post-nominals { font-size: 13px; font-weight: 400; }
  .qualification { margin-top: 9px; font-size: 13px; line-height: 16px; }
  .contact-list { list-style: none; margin-top: 26px; font-size: 13px; line-height: 16px; }
  .contact-list li { display: flex; justify-content: flex-end; align-items: center; gap: 4px; }
  .contact-list svg { width: 11px; height: 11px; }
  .social-handle {
    display: flex; justify-content: flex-end; align-items: center; gap: 5px;
    margin-top: 24px; font-size: 12px; line-height: 16px;
  }
  .social-dot { width: 7px; height: 7px; background: var(--white); border-radius: 50%; }

  .brand {
    position: absolute;
    left: 0; right: 0; top: 50px;
    display: flex; justify-content: center; align-items: center; gap: 12px;
  }
  .brand-circle { width: 60px; height: 60px; border: 2px solid var(--logo-grey); border-radius: 50%; }
  .brand-name { font-size: 24px; font-weight: 400; color: var(--logo-grey); letter-spacing: 0.5px; }

  .service-band {
    position: absolute; left: 0; right: 0; top: 151px; height: 28px;
    background: var(--sky); color: var(--white);
    font-size: 13px; text-align: center; line-height: 28px; letter-spacing: 0.2px;
  }
  .treatment-band {
    position: absolute; left: 0; right: 0; top: 183px; height: 46px;
    background: var(--mist-grey); color: var(--white);
    font-size: 13.5px; text-align: center; line-height: 16px; padding-top: 7px;
  }
  .treatment-band .sep { margin: 0 6px; font-size: 9px; vertical-align: 1px; }
</style>
</head>
<body>
  <section class="card card-front">
    <div class="portrait-art" role="img" aria-label="Flowing blue wave illustration of a head in profile"></div>
    <div class="details">
      <h1 class="doctor-name">Dr Mireille Kasten <span class="post-nominals">MRCPCH MD</span></h1>
      <p class="qualification">Australasian Diploma of<br>Aesthetic Medicine</p>
      <ul class="contact-list">
        <li>0800 555 019
          <svg viewBox="0 0 12 12" aria-hidden="true"><path d="M3 1l2 2.5-1.2 1.2c.6 1.3 1.6 2.3 2.9 2.9L8 6.4 10.5 8.4 9.3 10.8C5 10.5 1.5 7 1.2 2.7z" fill="none" stroke="#fff" stroke-width="1.2" stroke-linejoin="round"/></svg>
        </li>
        <li>mireille@lorvena.co.nz
          <svg viewBox="0 0 12 12" aria-hidden="true"><rect x="0.5" y="2.5" width="11" height="7.5" fill="#fff"/><path d="M0.5 2.5L6 7l5.5-4.5" fill="none" stroke="#0f7dcb" stroke-width="1"/></svg>
        </li>
        <li>www.lorvena.co.nz
          <svg viewBox="0 0 12 12" aria-hidden="true"><g fill="none" stroke="#fff" stroke-width="1"><circle cx="6" cy="6" r="5.2"/><ellipse cx="6" cy="6" rx="2.3" ry="5.2"/><path d="M0.8 6h10.4M1.6 3.4h8.8M1.6 8.6h8.8"/></g></svg>
        </li>
      </ul>
      <p class="social-handle"><span class="social-dot" aria-hidden="true"></span>@lorvena.aesthetics</p>
    </div>
  </section>

  <section class="card card-back">
    <div class="brand">
      <span class="brand-circle" aria-hidden="true"></span>
      <span class="brand-name">Lorvena Aesthetic Doctor</span>
    </div>
    <div class="service-band">HOME AND SPA BASED TREATMENTS</div>
    <div class="treatment-band">
      Dermal injectables<span class="sep">●</span>Plasma facials<span class="sep">●</span>Microneedling<br>
      Skin boosters<span class="sep">●</span>Excessive sweating
    </div>
  </section>
</body>
</html>
```